Design refresh of existing HR Application

Talvora is an HR & Payroll processing software, already in use by thousands of people. It is a feature packed, enterprise-grade software that is also simple and user friendly. Visit us at https://talvora.example

Seeking a refresh of the app design/UI.

Key objectives are to make it "sleeker", more professional and polished, whist still retaining functionality. Not intended to be a massive overhaul, but more of reorganization and improvements on design elements.

You may login to our demo account to see the app live.
https://app.talvora.example/login
User: demo@talvora.example
Password: Bex47

Target Market(s)

HR Managers, business administrators/owners and employees.

Industry/Entity Type

Business Software

Number of Pages Required

4 page

Font styles to use
Other font styles liked:
• Lato

Colors
0255a3
3377b5
00a990
33b8a4
f37122
faa54b

Requirements
Must have
• Must retain the current functionality on each page.
Nice to have
• Fine to suggest changes to colors, font sizes, card designs, moving sections around and any other design element changes.

```html
<!DOCTYPE html>
<html lang="en">
<head>
<meta charset="utf-8">
<title>Talvora – Weekly Calendar</title>
<link href="https://fonts.googleapis.com/css2?family=Poppins:wght@400;500;600&display=swap" rel="stylesheet">
<style>
:root{
  --blue:#0255a3;
  --blue-2:#3377b5;
  --blue-active:#1765b3;
  --teal:#00a990;
  --teal-2:#33b8a4;
  --orange:#f37122;
  --amber:#faa54b;
  --bg:#eef4fb;
  --rail:#f3f5f8;
  --ink:#2b2f38;
  --muted:#8a919c;
  --line:#e3e7ed;
  --sky:#1ba4dc;
  --pill:#2f74b8;
  --pill-off:#e6e8eb;
}
*{box-sizing:border-box;margin:0;padding:0}
html,body{width:1200px;height:844px;overflow:hidden}
body{font-family:"Poppins",sans-serif;color:var(--ink);background:var(--bg)}
.canvas{position:relative;width:1200px;height:844px;background:var(--bg)}
.abs{position:absolute}
.rail{left:0;top:0;width:49px;height:844px;background:var(--rail)}
.rail-icon{position:absolute;left:14px;width:20px;height:20px}
.rail-active{position:absolute;left:0;top:228px;width:3px;height:47px;background:var(--orange)}
.sidebar{left:49px;top:0;width:171px;height:844px;background:linear-gradient(180deg,#0358a8,#0a4f9a)}
.brand{position:absolute;top:40px;left:0;width:171px;text-align:center;color:#fff;font-weight:500;font-size:14px;letter-spacing:2px;display:flex;justify-content:center;align-items:center;gap:8px}
.brand-mark{width:14px;height:14px;background:#fff;border-radius:2px}
.nav{position:absolute;top:130px;left:0;width:171px;list-style:none}
.nav li{height:51px;line-height:51px;padding-left:24px;color:#fff;font-weight:600;font-size:14.5px}
.nav li.active{background:var(--blue-active)}
.header{left:220px;top:0;width:980px;height:89px;background:#fff}
.company{left:250px;top:38px;font-size:15px;font-weight:500;letter-spacing:.3px;color:#3a3f48}
.caret{display:inline-block;width:6px;height:6px;border-right:1.5px solid currentColor;border-bottom:1.5px solid currentColor;transform:rotate(45deg);margin-left:10px;vertical-align:3px}
.lang{left:794px;top:38px;font-size:15px;font-weight:500;display:flex;align-items:center;gap:7px}
.flag{width:18px;height:12px;background:linear-gradient(#243d8c,#c8102e);border-radius:1px}
.help{left:908px;top:22px;width:50px;height:50px;border-radius:50%;background:var(--teal-2);display:flex;align-items:center;justify-content:center}
.avatar{left:967px;top:23px;width:48px;height:48px;border-radius:50%;background:linear-gradient(135deg,#8a6a55,#3d4b5c)}
.user{left:1027px;top:32px}
.user .name{font-size:15.5px;font-weight:500;color:#3a3f48}
.user .role{font-size:11px;color:#555}
.user-caret{left:1167px;top:42px;color:#333}
.tab{top:122px;font-size:12.5px;font-weight:600;color:#222}
.tab.on{left:308px;top:112px;width:84px;height:36px;border-radius:18px;background:var(--teal);color:#fff;line-height:36px;text-align:center}
.tz{left:988px;top:112px;width:188px;height:34px;border:1.5px solid #cfd6df;border-radius:17px;font-size:13px;line-height:31px;padding-left:16px;color:#3a3f48;background:var(--bg)}
.tz .caret{position:absolute;right:14px;top:11px;margin:0;width:5px;height:5px}
.stat{top:174px;width:228px;height:70px;background:#fff;border-radius:6px;box-shadow:0 6px 14px rgba(20,60,120,.07);display:flex;align-items:center;padding-left:22px;gap:14px}
.stat svg{flex:none}
.stat .num{font-size:32px;font-weight:400;color:#333;letter-spacing:1px}
.stat .lbl{font-size:12px;line-height:13px;font-weight:500;color:#333}
.filter{top:284px;height:35px;border:1.5px solid #cfd6df;border-radius:3px;font-size:13px;line-height:32px;padding-left:16px;color:#3a3f48;background:var(--bg)}
.filter .caret{position:absolute;right:10px;top:11px;margin:0;width:5px;height:5px}
.panel{left:258px;top:347px;width:920px;height:468px;background:#fff}
.month{top:393px;font-size:14.5px;font-weight:500}
.arrow-btn{top:389px;width:26px;height:26px;border-radius:50%;background:#eceef1;display:flex;align-items:center;justify-content:center}
.day{top:376px;width:80px;text-align:center;font-size:12.5px}
.day .dn{color:var(--sky);font-weight:600}
.day .dd{margin-top:2px;color:#333}
.day .du{margin-top:4px;color:var(--muted)}
.duty{left:512px;top:417px;font-size:12.5px;color:var(--muted)}
.hrule{height:1px;background:var(--line)}
.vrule{width:1px;background:var(--line)}
.hours-h{left:507px;top:447px;width:60px;text-align:center;font-size:12px;font-weight:500}
.emp{left:279px;width:226px;height:40px}
.emp .pic{position:absolute;left:0;top:4px;width:32px;height:32px;border-radius:50%;background:#e4e6ea;display:flex;align-items:center;justify-content:center}
.emp .en{position:absolute;left:39px;top:1px;font-size:12.5px;font-weight:500;color:#333}
.emp .eb{position:absolute;left:39px;top:20px;font-size:13px;color:#555}
.emp .dots{position:absolute;right:5px;top:12px;width:3px;height:14px;background:radial-gradient(circle,#777 1.3px,transparent 1.6px) 0 0/3px 5px}
.hrs{left:507px;width:60px;text-align:center;font-size:13.5px;color:var(--muted)}
.shift{width:69px;height:21px;border-radius:3px;font-size:10.5px;line-height:21px;text-align:center;color:#fff;background:var(--pill)}
.shift.off{background:var(--pill-off);color:#333}
.scroll{left:1168px;top:629px;width:4px;height:84px;background:#e3e6ea;border-radius:2px}
</style>
</head>
<body>
<div class="canvas">

  <div class="abs rail"></div>
  <div class="rail-active"></div>
  <svg class="rail-icon" style="top:139px" viewBox="0 0 20 20"><path d="M2 14a8 8 0 0 1 16 0z" fill="#9aa1ab"/></svg>
  <svg class="rail-icon" style="top:190px" viewBox="0 0 20 20"><circle cx="8" cy="6" r="4" fill="#9aa1ab"/><path d="M1 17c0-5 14-5 14 0z" fill="#9aa1ab"/></svg>
  <svg class="rail-icon" style="top:239px" viewBox="0 0 20 20"><rect x="2" y="4" width="16" height="14" rx="1.5" fill="var(--orange)"/><rect x="4" y="9" width="12" height="7" fill="#fff" opacity=".45"/></svg>
  <svg class="rail-icon" style="top:290px" viewBox="0 0 20 20"><rect x="3" y="2" width="12" height="16" rx="1.5" fill="#9aa1ab"/><circle cx="14" cy="14" r="4" fill="#7d848e"/></svg>
  <svg class="rail-icon" style="top:342px" viewBox="0 0 20 20"><rect x="2" y="4" width="14" height="14" fill="#9aa1ab"/><circle cx="15" cy="15" r="3.5" fill="#7d848e"/></svg>
  <svg class="rail-icon" style="top:393px" viewBox="0 0 20 20"><rect x="2" y="11" width="3" height="7" fill="#9aa1ab"/><rect x="7" y="8" width="3" height="10" fill="#9aa1ab"/><rect x="12" y="5" width="3" height="13" fill="#9aa1ab"/></svg>
  <svg class="rail-icon" style="top:443px" viewBox="0 0 20 20"><circle cx="10" cy="10" r="8" fill="none" stroke="#9aa1ab" stroke-width="2"/><circle cx="10" cy="10" r="3.5" fill="#9aa1ab"/></svg>
  <svg class="rail-icon" style="top:493px" viewBox="0 0 20 20"><path d="M4 2h8l4 4v12H4z" fill="#9aa1ab"/></svg>
  <svg class="rail-icon" style="top:546px" viewBox="0 0 20 20"><circle cx="10" cy="10" r="7" fill="none" stroke="#9aa1ab" stroke-width="4" stroke-dasharray="3 2.5"/><circle cx="10" cy="10" r="3" fill="#9aa1ab"/></svg>

  <nav class="abs sidebar">
    <div class="brand"><span class="brand-mark"></span>KESTRA</div>
    <ul class="nav">
      <li>Dashboard</li>
      <li>Employees</li>
      <li class="active">Calendar</li>
      <li>Expenses</li>
      <li>Payroll</li>
      <li>Performance</li>
      <li>Engagement</li>
      <li>Reports</li>
      <li>Settings</li>
    </ul>
  </nav>

  <header class="abs header"></header>
  <div class="abs company">PT KESTRA MANUFACTURING (DEMO)<span class="caret"></span></div>
  <div class="abs lang"><span class="flag"></span>English<span class="caret" style="margin-left:2px;width:5px;height:5px"></span></div>
  <div class="abs help"><svg width="24" height="24" viewBox="0 0 24 24"><circle cx="12" cy="12" r="10" fill="none" stroke="#fff" stroke-width="1.8"/><path d="M9 9.5a3 3 0 1 1 4 2.8c-.7.3-1 .8-1 1.5v.7" fill="none" stroke="#fff" stroke-width="1.8"/><circle cx="12" cy="17.5" r="1.1" fill="#fff"/></svg></div>
  <div class="abs avatar" role="img" aria-label="Profile photo of the signed-in HR administrator"></div>
  <div class="abs user"><div class="name">DARIAN VOLKE</div><div class="role">HR Administrator</div></div>
  <div class="abs user-caret"><span class="caret" style="margin:0"></span></div>

  <div class="abs tab" style="left:249px">DAILY</div>
  <div class="abs tab on">WEEKLY</div>
  <div class="abs tab" style="left:414px">MONTHLY</div>
  <div class="abs tab" style="left:519px">LIST</div>
  <div class="abs tab" style="left:594px">GEO-TAGGING</div>
  <div class="abs tz">Current Time Zone<span class="caret"></span></div>

  <div class="abs stat" style="left:246px">
    <svg width="40" height="40" viewBox="0 0 40 40"><rect x="3" y="7" width="28" height="27" rx="3" fill="none" stroke="var(--blue)" stroke-width="2.2"/><path d="M3 14h28M10 4v6M24 4v6" stroke="var(--blue)" stroke-width="2.2"/><path d="M14 18l2 4 4.5.5-3.3 3 1 4.5-4.2-2.3-4 2.3.9-4.5-3.3-3 4.5-.5z" fill="var(--blue)"/><circle cx="31" cy="31" r="7" fill="#fff" stroke="var(--blue)" stroke-width="2.2"/><path d="M27.5 31l2.5 2.5 4.5-4.5" fill="none" stroke="var(--blue)" stroke-width="2"/></svg>
    <span class="num">12</span><span class="lbl" style="margin-left:-12px">EVENT<br>AMENDMENT</span>
  </div>
  <div class="abs stat" style="left:481px">
    <svg width="40" height="40" viewBox="0 0 40 40"><path d="M3 20a17 16 0 0 1 34 0c-3-3-6-3-8.5 0-2.5-3-6-3-8.5 0-2.5-3-6-3-8.5 0C9 17 6 17 3 20z" fill="none" stroke="var(--teal)" stroke-width="2.2"/><path d="M20 4v26a4 4 0 0 1-8 0" fill="none" stroke="var(--teal)" stroke-width="2.2"/></svg>
    <span class="num">03</span><span class="lbl">LEAVE<br>REQUESTS</span>
  </div>
  <div class="abs stat" style="left:716px;padding-left:28px">
    <svg width="40" height="40" viewBox="0 0 40 40"><path d="M34 14A16 16 0 1 1 26 5" fill="none" stroke="var(--orange)" stroke-width="3"/><path d="M27 1l6 5-7 3" fill="var(--orange)"/><path d="M20 11v10l6 4" fill="none" stroke="var(--orange)" stroke-width="3"/></svg>
    <span class="num">07</span><span class="lbl">EVENT<br>REQUESTS</span>
  </div>
  <div class="abs stat" style="left:949px;padding-left:32px">
    <svg width="34" height="42" viewBox="0 0 34 42"><rect x="12" y="2" width="19" height="28" fill="#fff" stroke="var(--blue-2)" stroke-width="2"/><rect x="7" y="6" width="19" height="28" fill="#fff" stroke="var(--blue-2)" stroke-width="2"/><path d="M2 10h19v30l-3-2-3 2-3-2-3 2-3-2-4 2z" fill="#fff" stroke="var(--blue-2)" stroke-width="2"/><text x="11.5" y="30" font-size="14" font-weight="600" text-anchor="middle" fill="var(--blue-2)" font-family="Poppins,sans-serif">$</text></svg>
    <span class="num">02</span><span class="lbl">PAYROLLS<br>PENDING</span>
  </div>

  <div class="abs filter" style="left:255px;width:153px">Search by name<span class="caret"></span></div>
  <div class="abs filter" style="left:416px;width:101px;padding-left:13px">Department<span class="caret"></span></div>
  <div class="abs filter" style="left:524px;width:104px">Branch<span class="caret"></span></div>
  <div class="abs filter" style="left:636px;width:103px">Group<span class="caret"></span></div>
  <div class="abs filter" style="left:744px;width:102px">Activity<span class="caret"></span></div>
  <div class="abs filter" style="left:853px;width:103px;padding-left:13px">Activity Type<span class="caret" style="right:6px"></span></div>
  <div class="abs filter" style="left:963px;width:103px">Positions<span class="caret"></span></div>
  <div class="abs filter" style="left:1073px;width:103px;padding-left:13px">First Name<span class="caret"></span></div>

  <section class="abs panel"></section>
  <div class="abs arrow-btn" style="left:279px"><svg width="8" height="10" viewBox="0 0 8 10"><path d="M6 1L2 5l4 4" fill="none" stroke="#333" stroke-width="1.5"/></svg></div>
  <div class="abs month" style="left:359px">MAY</div>
  <div class="abs arrow-btn" style="left:439px"><svg width="8" height="10" viewBox="0 0 8 10"><path d="M2 1l4 4-4 4" fill="none" stroke="#333" stroke-width="1.5"/></svg></div>

  <div class="abs duty">On DUTY</div>
  <div class="abs day" style="left:572px"><div class="dn">MON</div><div class="dd">25/5/20</div><div class="du">140</div></div>
  <div class="abs day" style="left:660px"><div class="dn">TUE</div><div class="dd">26/5/20</div><div class="du">140</div></div>
  <div class="abs day" style="left:746px"><div class="dn">WED</div><div class="dd">27/5/20</div><div class="du">113</div></div>
  <div class="abs day" style="left:834px"><div class="dn">THU</div><div class="dd">28/5/20</div><div class="du">134</div></div>
  <div class="abs day" style="left:916px"><div class="dn">FRI</div><div class="dd">29/5/20</div><div class="du">160</div></div>
  <div class="abs day" style="left:996px"><div class="dn">SAT</div><div class="dd">30/5/20</div><div class="du">52</div></div>
  <div class="abs day" style="left:1083px"><div class="dn">SUN</div><div class="dd">31/5/20</div><div class="du">52</div></div>
  <div class="abs hrule" style="left:282px;top:436px;width:860px"></div>

  <div class="abs hours-h">HOURS</div>
  <div class="abs vrule" style="left:507px;top:447px;height:329px"></div>
  <div class="abs vrule" style="left:567px;top:447px;height:329px"></div>
  <div class="abs vrule" style="left:655px;top:447px;height:329px"></div>
  <div class="abs vrule" style="left:742px;top:447px;height:329px"></div>
  <div class="abs vrule" style="left:828px;top:447px;height:329px"></div>
  <div class="abs vrule" style="left:916px;top:447px;height:329px"></div>
  <div class="abs vrule" style="left:1000px;top:447px;height:329px"></div>
  <div class="abs vrule" style="left:1081px;top:447px;height:329px"></div>

  <div class="abs hrule" style="left:567px;top:533px;width:589px"></div>
  <div class="abs hrule" style="left:567px;top:595px;width:589px"></div>
  <div class="abs hrule" style="left:567px;top:657px;width:589px"></div>
  <div class="abs hrule" style="left:567px;top:720px;width:589px"></div>
  <div class="abs hrule" style="left:315px;top:526px;width:122px"></div>
  <div class="abs hrule" style="left:315px;top:589px;width:122px"></div>
  <div class="abs hrule" style="left:315px;top:652px;width:122px"></div>
  <div class="abs hrule" style="left:315px;top:715px;width:122px"></div>

  <div class="abs emp" style="top:479px"><div class="pic"><svg width="12" height="12" viewBox="0 0 12 12"><circle cx="6" cy="4" r="2.5" fill="#a9aeb6"/><path d="M1.5 11c0-4 9-4 9 0z" fill="#a9aeb6"/></svg></div><div class="en">1 EMPLOYEE</div><div class="eb">Branch 8 | Department 6</div><div class="dots"></div></div>
  <div class="abs emp" style="top:542px"><div class="pic"><svg width="12" height="12" viewBox="0 0 12 12"><circle cx="6" cy="4" r="2.5" fill="#a9aeb6"/><path d="M1.5 11c0-4 9-4 9 0z" fill="#a9aeb6"/></svg></div><div class="en">10 EMPLOYEE</div><div class="eb">Branch 8 | Department 7</div><div class="dots"></div></div>
  <div class="abs emp" style="top:605px"><div class="pic"><svg width="12" height="12" viewBox="0 0 12 12"><circle cx="6" cy="4" r="2.5" fill="#a9aeb6"/><path d="M1.5 11c0-4 9-4 9 0z" fill="#a9aeb6"/></svg></div><div class="en">100 EMPLOYEE</div><div class="eb">Branch 8 | Department 6</div><div class="dots"></div></div>
  <div class="abs emp" style="top:668px"><div class="pic"><svg width="12" height="12" viewBox="0 0 12 12"><circle cx="6" cy="4" r="2.5" fill="#a9aeb6"/><path d="M1.5 11c0-4 9-4 9 0z" fill="#a9aeb6"/></svg></div><div class="en">101 EMPLOYEE</div><div class="eb">Branch 8 | Department 10</div><div class="dots"></div></div>
  <div class="abs emp" style="top:731px"><div class="pic"><svg width="12" height="12" viewBox="0 0 12 12"><circle cx="6" cy="4" r="2.5" fill="#a9aeb6"/><path d="M1.5 11c0-4 9-4 9 0z" fill="#a9aeb6"/></svg></div><div class="en">102 EMPLOYEE</div><div class="eb">Branch 8 | Department 9</div><div class="dots"></div></div>

  <div class="abs hrs" style="top:491px">40</div>
  <div class="abs hrs" style="top:554px">30</div>
  <div class="abs hrs" style="top:617px">00</div>
  <div class="abs hrs" style="top:680px">00</div>
  <div class="abs hrs" style="top:743px">00</div>

  <div class="abs shift" style="left:577px;top:490px">10:00-19:00</div>
  <div class="abs shift" style="left:665px;top:490px">10:00-19:00</div>
  <div class="abs shift" style="left:750px;top:490px">10:00-19:00</div>
  <div class="abs shift" style="left:837px;top:490px">10:00-19:00</div>
  <div class="abs shift" style="left:924px;top:490px">10:00-19:00</div>
  <div class="abs shift off" style="left:1005px;top:490px">10:00-19:00</div>
  <div class="abs shift off" style="left:1088px;top:490px">10:00-19:00</div>

  <div class="abs shift" style="left:577px;top:555px">10:00-18:00</div>
  <div class="abs shift" style="left:665px;top:555px">10:00-18:00</div>
  <div class="abs shift" style="left:750px;top:555px">10:00-18:00</div>
  <div class="abs shift" style="left:837px;top:555px">18:00-23:00</div>
  <div class="abs shift" style="left:924px;top:555px">18:00-23:00</div>
  <div class="abs shift off" style="left:1005px;top:555px">10:00-19:00</div>
  <div class="abs shift off" style="left:1088px;top:555px">10:00-19:00</div>

  <div class="abs scroll"></div>
</div>
</body>
</html>
```